National Dart League Needs a Graphic Design

We need a graphic design for an established company named 'TripleFern' for our national (US) singles dart league. We now have hundreds of players in multiple states.

Our league is based on international long format darts (see KWN, TLM) and provides our members with the ability to participate with other players in other states. We have regional playoffs and offer sponsorships for our playoff winners to large dart tournaments.

We're looking for an image that showcases the national scope of our league and is suitable for social media campaigns. This will be used to market our league to new areas.

Industry/Entity Type

Graphic Design

```html
<!DOCTYPE html>
<html lang="en">
<head>
<meta charset="utf-8">
<title>TripleFern National (US) Singles Dart League</title>
<link rel="stylesheet" href="https://fonts.googleapis.com/css2?family=Anton&family=Oswald:wght@600&display=swap">
<style>
  :root {
    --stage: #2e2019;
    --banner-black: #0a0706;
    --smoke: #2a2422;
    --band-white: #ffffff;
    --ink: #0b0b0b;
    --logo-grey: #7d786e;
    --flame-core: #ffb43a;
    --flame-mid: #e3571a;
    --flame-deep: #7a1c06;
    --board-cream: #f1e3bf;
    --eagle-tone: #a89c8c;
  }
  html, body {
    margin: 0;
    width: 1200px;
    height: 694px;
    overflow: hidden;
    background: var(--stage);
  }
  .banner {
    position: absolute;
    left: 124px;
    top: 108px;
    width: 952px;
    height: 477px;
    overflow: hidden;
    background:
      radial-gradient(ellipse 380px 200px at 420px 60px, var(--smoke), transparent 70%),
      radial-gradient(ellipse 300px 160px at 520px 430px, var(--smoke), transparent 70%),
      var(--banner-black);
  }
  .title-band {
    position: absolute;
    left: 0;
    top: 100px;
    width: 640px;
    height: 277px;
    background: linear-gradient(90deg, var(--band-white) 0%, var(--band-white) 86%, rgba(255,255,255,0) 100%);
  }
  .eagle {
    position: absolute;
    top: 112px;
    width: 76px;
    height: 62px;
    border-radius: 40% 40% 50% 50%;
    background: radial-gradient(ellipse at 50% 60%, var(--eagle-tone), rgba(168,156,140,0.25) 70%, transparent 75%);
  }
  .eagle--left { left: 46px; }
  .eagle--right { left: 330px; }
  .brand {
    position: absolute;
    left: 136px;
    top: 138px;
    display: flex;
    align-items: center;
    gap: 8px;
    font-family: "Oswald", sans-serif;
    font-weight: 600;
    font-size: 26px;
    letter-spacing: 1px;
    color: var(--logo-grey);
  }
  .brand__dot {
    width: 14px;
    height: 14px;
    border-radius: 50%;
    background: var(--logo-grey);
  }
  .headline {
    position: absolute;
    left: 42px;
    top: 186px;
    margin: 0;
    font-family: "Anton", sans-serif;
    font-weight: 400;
    font-size: 62px;
    line-height: 52px;
    color: var(--ink);
    text-transform: uppercase;
    letter-spacing: 0.5px;
  }
  .headline span { display: block; }
  .board-art {
    position: absolute;
    left: 476px;
    top: 20px;
    width: 480px;
    height: 470px;
    border-radius: 50%;
    background:
      radial-gradient(circle at 50% 52%, var(--board-cream) 0%, #c9b48a 26%, #1c1410 40%, var(--flame-deep) 47%, var(--flame-mid) 53%, var(--flame-core) 57%, var(--flame-mid) 62%, rgba(122,28,6,0.5) 68%, transparent 74%);
  }
</style>
</head>
<body>
  <main class="banner">
    <div class="title-band"></div>
    <div class="board-art" role="img" aria-label="Dartboard engulfed in a ring of flames"></div>
    <div class="eagle eagle--left" role="img" aria-label="Eagle carrying an American flag"></div>
    <div class="eagle eagle--right" role="img" aria-label="Eagle carrying an American flag"></div>
    <div class="brand"><span class="brand__dot"></span>TripleFern</div>
    <h1 class="headline">
      <span>National (US)</span>
      <span>Singles</span>
      <span>Dart League</span>
    </h1>
  </main>
</body>
</html>
```